Book Cover Design Project

I need a book cover for a book that we will be releasing in the next few months.

It is a business book aimed at small businesses and people who want to escape the 9 - 5 and start their own business.

We want it to look similar to: http://www.tolvanbrook.example/wp-content/uploads/2010/03/fold-up.jpg and also the book designs that I have uploaded images for.

I quite like the grey / charcoal background and the bright lime green colours from the Quiet Harbor logo that I have attached. However, anything bright would be good - I am prepared to be flexible with colours. The books I have attached are a high impact as well - being bright blue with white black font with a really cool font.

The book is titled:

The Lantern Shop Plan

By Dale Vortan

Still thinking of the tagline, for now just use "Start an Online Business in no time at all"

Room for a quote/testimonial on the front of the book at the bottom, and as well on the back.

For the back cover text just use dummy text and my photo that is attached for now as well.

Barcode ISBN on the back at the bottom - price will be $19.95

Needs to be in PSD so we can change the text from our end.

I really want to get a good template made that I can edit the text for as we are still developing the book, but I want to get the book cover done so I can start advertising that it will be arriving soon.

There will probably be alterations that I need help with later down the track so looking to work with someone closely on this, and I will pay you for any extra time down the track..

Sizes will probably be around: I think 20.5cm tall and 14cm wide would be good..

Not sure how thick for the spine, it will depend on how many words get cut off, but as an estimate probably 1.5CM..
Updates

Just added some more detail to the brief.. Please read it carefully.

Target Market(s)

small business owners, professionals who want to start their own business, soon to be entrepreneurs, entrepreneurs

Industry/Entity Type

Advertising

Requirements
Must have
• The Lantern Shop Plan

and Dale Vortan must be prominent.

Tag line should be look cool under the title.

Must be very modern and cool. Needs to catch people's eyes so needs to be really punchy.

Nice to have
• Maybe a clock or stopwatch icon would be cool to add in there so it isn't just plain.. Similar to like how the books have a cool icon with them that I have attached in the uploaded images.
Should not have
• I like simplicity, artistic and very high impact. It really needs to draw you in and catch your eye.

Don't use plain boring fonts. Although I like simplicity slick design is very important - I dont want it to be boring - it has to look high quality and expensive. Therefore do not use fonts like Arial, Times New Roman those really boring fonts that make it look cheap. If I was going to do something like that then I might as well do it myself.

If you want to see the quality of things that I am usually involved with look at the artwork for one of my events that I run called Daybreaker: http://www.daybreaker.example/daybreaker-festival-anthems-ft-loomsparrow-harvest-night-eve-metro-report/

That will give you an idea of what type of quality things that I am involved with, so you need to be up for the task..

```html
<!DOCTYPE html>
<html lang="en">
<head>
<meta charset="utf-8">
<title>The Lantern Shop Plan — Cover</title>
<link rel="stylesheet" href="https://fonts.googleapis.com/css2?family=Bebas+Neue&family=Oswald:wght@500&family=Open+Sans:ital,wght@0,400;1,400&display=swap">
<style>
  :root{
    --stage:#0b0b0b;
    --cover:#1d1d1d;
    --cover-edge:#262626;
    --lime:#f2e400;
    --white:#f4f4f4;
    --muted:#bdbdbd;
    --band:#3a3a3a;
  }
  *{box-sizing:border-box;margin:0;padding:0}
  html,body{width:1200px;height:920px;overflow:hidden;background:var(--stage)}
  .stage{width:1200px;height:920px;display:flex;align-items:center;justify-content:center;gap:44px}
  .cover{width:519px;height:760px;background:var(--cover);border:1px solid var(--cover-edge);position:relative;overflow:hidden}

  .name-dot{border-radius:50%;background:var(--lime)}
  .book-name{font-family:'Bebas Neue',sans-serif;font-weight:400;color:var(--lime);text-align:center;line-height:.9}
  .book-name span{display:block}
  .rule{height:6px;background:var(--lime)}
  .quote{font-family:'Open Sans',sans-serif;font-style:italic;color:var(--muted);text-align:center}
  .quote cite{display:block;font-style:normal;font-family:'Oswald',sans-serif;font-weight:500;letter-spacing:2px;text-transform:uppercase;color:var(--white);margin-top:6px}

  /* Front cover */
  .front{display:flex;flex-direction:column;align-items:center;padding:34px 52px 36px}
  .front .author{font-family:'Oswald',sans-serif;font-weight:500;font-size:15px;letter-spacing:4px;color:var(--muted);text-transform:uppercase}
  .front .name-dot{width:58px;height:58px;margin-top:24px}
  .front .book-name{font-size:98px;margin-top:18px}
  .front .rule{width:100%;margin-top:20px}
  .front .tagline{width:100%;margin-top:12px;background:var(--band);color:var(--white);font-family:'Oswald',sans-serif;font-weight:500;font-size:15px;letter-spacing:1.5px;text-transform:uppercase;text-align:center;padding:8px 6px}
  .front .quote{margin-top:auto;font-size:13px;line-height:1.5}
  .front .quote cite{font-size:11px}

  /* Back cover */
  .back{display:grid;grid-template-columns:238px 1fr;column-gap:26px;padding:32px 30px 58px}
  .back .photo-rule{height:4px;background:var(--lime);margin-bottom:6px}
  .back .photo{width:100%;height:226px;background:linear-gradient(160deg,#d9d9d9 0%,#8a8a8a 55%,#3c3c3c 100%)}
  .back .blurb{font-family:'Open Sans',sans-serif;font-size:12px;line-height:1.55;color:var(--white);margin-top:16px}
  .back .blurb p+p{margin-top:9px}
  .back .side{display:flex;flex-direction:column;align-items:center}
  .back .name-dot{width:44px;height:44px;margin-top:8px}
  .back .book-name{font-size:58px;margin-top:14px}
  .back .side .rule{width:100%;margin-top:16px}
  .back .quote{margin-top:20px;font-size:12px;line-height:1.5}
  .back .quote cite{font-size:10px}
  .back .price{margin-top:auto;font-family:'Oswald',sans-serif;font-weight:500;font-size:22px;letter-spacing:1px;color:var(--lime)}
  .back .footer-rule{position:absolute;left:30px;right:30px;bottom:34px;height:5px;background:var(--lime)}
</style>
</head>
<body>
<main class="stage">

  <section class="cover front" aria-label="Front cover">
    <p class="author">Dale Vortan</p>
    <div class="name-dot" aria-hidden="true"></div>
    <h1 class="book-name">
      <span>The</span>
      <span>Lantern</span>
      <span>Shop</span>
      <span>Plan</span>
    </h1>
    <div class="rule"></div>
    <p class="tagline">Start an Online Business in no time at all</p>
    <blockquote class="quote">“Clear, fast and practical. The best small business guide I have read this year.”<cite>Reader Review</cite></blockquote>
  </section>

  <section class="cover back" aria-label="Back cover">
    <div class="column">
      <div class="photo-rule"></div>
      <div class="photo" role="img" aria-label="Author portrait of Dale Vortan"></div>
      <div class="blurb">
        <p>Start small, think clearly and build a business that runs while you live your life. This plan walks you through every step, from a first idea to a shop that earns each day. Each chapter is short, practical and made to be read in a few quiet minutes.</p>
        <p>Test the idea, set up the shop, find buyers and grow with calm focus. No jargon, no fluff, only the steps that work. Build it once, then let it work.</p>
        <p>Leave the desk job behind and learn how real owners plan their week, price their goods and keep customers coming back again and again.</p>
      </div>
    </div>
    <div class="side">
      <div class="name-dot" aria-hidden="true"></div>
      <h2 class="book-name">
        <span>The</span>
        <span>Lantern</span>
        <span>Shop</span>
        <span>Plan</span>
      </h2>
      <div class="rule"></div>
      <blockquote class="quote">“A calm, simple path from idea to income.”<cite>Early Reader</cite></blockquote>
      <p class="price">$19.95</p>
    </div>
    <div class="footer-rule"></div>
  </section>

</main>
</body>
</html>
```